Elegant wordpress web page for wedding rental of hand sanitizers

We want to rent our hand sanitizing towers out for high-end weddings. We need a very elegant, sophisticated page that describes our offering. You can see an ugly first draft here: purvant.com/weddings
Target Market(s)
Wedding planners, wedding parents
Number of Pages Required
1 page
Font styles to use
Serif
Script
Colors
Designer to choose colors to be used in the design.
Requirements
Nice to have
- Two wedding-related sites for inspiration: lacetrellisweddings-dot-com and fennoreventservices-dot-com

```html
<!DOCTYPE html>
<html lang="en">
<head>
<meta charset="utf-8">
<title>Purvant — Customized Hand Sanitizers for Weddings</title>
<link href="https://fonts.googleapis.com/css2?family=Cormorant+Garamond:wght@500;600&family=Lora:wght@400;500;600&display=swap" rel="stylesheet">
<style>
:root{
  --ink:#2b2623;
  --ink-soft:#3d3632;
  --cream:#f7f1ea;
  --sand:#ebe1d0;
  --white:#ffffff;
  --hero-top:#b9ab9c;
  --hero-mid:#cbb9a2;
  --hero-floor:#c69a66;
}
*{box-sizing:border-box;margin:0;padding:0}
html,body{width:1200px;height:2183px;overflow:hidden}
body{font-family:'Lora',serif;color:var(--ink);background:var(--cream);position:relative}
section,header,footer{position:absolute;left:0;width:1200px}

.hero{top:0;height:549px;background:linear-gradient(180deg,var(--hero-top) 0%,var(--hero-mid) 45%,var(--hero-floor) 100%)}
.hero-photo{position:absolute;inset:0;background:
  radial-gradient(ellipse 260px 180px at 1130px 230px,rgba(255,255,255,.35),transparent),
  radial-gradient(ellipse 300px 160px at 230px 250px,rgba(120,140,90,.25),transparent),
  linear-gradient(180deg,rgba(170,160,150,.3),rgba(190,150,100,.25))}
.hero-stand{position:absolute;left:120px;top:155px;width:112px;height:394px;background:linear-gradient(180deg,#c9b6a8 0%,#b8a39a 45%,#e9e6e2 47%,#f2f0ec 100%)}
.nav{position:absolute;top:0;left:0;width:1200px;height:74px;border-bottom:1px solid rgba(255,255,255,.7)}
.brand{position:absolute;left:149px;top:25px;font-weight:600;font-size:19px;color:var(--white)}
.nav-links a{position:absolute;top:32px;font-size:11px;color:var(--white);text-decoration:none;letter-spacing:.2px;font-family:'Lora',serif}
.reserve{position:absolute;left:898px;top:27px;width:167px;height:23px;background:var(--white);border-radius:5px;font-size:12px;color:var(--ink);text-align:center;line-height:23px}
.hero-title{position:absolute;top:220px;left:0;width:1200px;text-align:center;font-family:'Cormorant Garamond',serif;font-weight:500;font-size:38px;line-height:60px;color:var(--white);letter-spacing:1px}

.intro{top:549px;height:709px;background:var(--cream)}
.intro h2{position:absolute;top:56px;left:0;width:1200px;text-align:center;font-weight:400;font-size:26px;line-height:31px;color:var(--ink-soft)}
.feature{position:absolute;top:146px;width:200px;text-align:center;font-size:13px;line-height:16px;color:var(--ink-soft)}
.feature svg{display:block;margin:0 auto 24px;height:76px}

.row h3{position:absolute;font-weight:400;font-size:22px;color:var(--ink-soft)}
.row p{position:absolute;font-size:15px;line-height:24px;color:var(--ink-soft)}
.btn{position:absolute;width:285px;height:40px;border:2px solid var(--ink-soft);border-radius:6px;font-size:19px;line-height:36px;text-align:center;color:var(--ink-soft)}
.photo{position:absolute;border-radius:6px}

.custom{top:900px;height:358px}
.spouts{top:1258px;height:369px;background:var(--sand)}
.care{top:1627px;height:385px;background:var(--cream)}

.footer{top:2012px;height:171px;background:var(--sand);font-size:17px;color:var(--ink-soft)}
.footer span{position:absolute;top:73px}
.social{position:absolute;top:2096px}
.social i{position:absolute;width:28px;height:28px;border-radius:50%;background:#141210}
</style>
</head>
<body>

<header class="hero">
  <div class="hero-photo" role="img" aria-label="Wedding reception hall with white chairs, floral arrangements and candles"></div>
  <div class="hero-stand" role="img" aria-label="Sanitizer tower topped with a couple's photo"></div>
  <nav class="nav">
    <div class="brand">Purvant</div>
    <div class="nav-links">
      <a style="left:292px">ABOUT</a>
      <a style="left:378px">PRODUCTS</a>
      <a style="left:486px">INDUSTRY SOLUTIONS</a>
      <a style="left:660px">CONTACT</a>
      <a style="left:761px">SEARCH</a>
    </div>
    <div class="reserve">MAKE A RESERVATION</div>
  </nav>
  <h1 class="hero-title">WELCOME YOUR GUESTS WITH<br>SOMETHING TRULY UNIQUE<br>-A CUSTOMIZED HAND SANITIZER-</h1>
</header>

<section class="intro">
  <h2>Why have a generic, industrial hand santisizer<br>when you could have something truly unique?</h2>
  <div class="feature" style="left:155px">
    <svg width="70" height="70" viewBox="0 0 70 70" fill="none" stroke="#141210" stroke-width="4" stroke-linecap="round" stroke-linejoin="round"><rect x="6" y="6" width="58" height="58" rx="6"/><path d="M35 50 V22 M24 33 L35 22 L46 33"/></svg>
    Customize the photo above the spout
  </div>
  <div class="feature" style="left:499px">
    <svg width="78" height="74" viewBox="0 0 78 74" fill="none" stroke="#141210" stroke-width="4"><rect x="6" y="12" width="52" height="52" transform="rotate(-12 32 38)"/><rect x="16" y="6" width="54" height="54" transform="rotate(-6 43 33)"/><path d="M28 48 L40 30 L52 46 M46 40 L54 32 L62 44"/><circle cx="34" cy="22" r="4"/></svg>
    Choose any size and shape and photo
  </div>
  <div class="feature" style="left:823px;width:240px">
    <svg width="68" height="68" viewBox="0 0 68 68" fill="none" stroke="#141210" stroke-width="4"><rect x="3" y="3" width="62" height="62" rx="4"/><path d="M22 12 V22 Q34 34 46 22 V12 L40 18 L34 12 L28 18 Z M34 30 V52 M20 42 H48 V52 H20 Z"/></svg>
    Choose from our standard spout decoration or design your own, We'll take care of producing and fitting it.
  </div>
</section>

<section class="row custom">
  <h3 style="left:150px;top:80px">Customize your sanitizer with any photo, any size, any shape</h3>
  <p style="left:150px;top:117px">Choose a photo of the happy couple, the proud parents, or anything else you wish<br>Choose any size or shape you wish, up to 24x36"<br>We take care of all production and customization</p>
  <div class="btn" style="left:150px;top:200px">Check price and availability</div>
  <div class="photo" style="left:790px;top:0;width:325px;height:325px;background:linear-gradient(135deg,#5d6a3e 0%,#b9b0a0 40%,#d8c9b4 70%,#e8d7c6 100%)" role="img" aria-label="Photo sanitizer tower at an outdoor ceremony aisle"></div>
</section>

<section class="row spouts">
  <div class="photo" style="left:188px;top:33px;width:145px;height:304px;background:linear-gradient(180deg,#d9cfc6 0%,#c7b9b0 55%,#efece8 60%,#e4e1dc 100%)" role="img" aria-label="Sanitizer tower with a wedding cake spout decoration"></div>
  <h3 style="left:456px;top:86px">Choose one of our standard spouts, or design your own</h3>
  <p style="left:456px;top:127px;width:620px">Choose one of our standard spouts - wedding cake, flower vase, or "just married" car<br>More spout decorations will be added each month<br>For an additional fee, our team of 3D designers will design, 3D print, and decorate a spout just for your event</p>
  <div class="btn" style="left:456px;top:239px">Check price and availability</div>
</section>

<section class="row care">
  <h3 style="left:149px;top:94px">Greet your guests with an act of care</h3>
  <p style="left:149px;top:133px;width:590px">Make your friends and family feel welcome and safe with a rugged, durable hand sanitizer from Purvant<br>Our battery-powered dispensers are reliable, wireless, and touchless<br>Filled with your choice from our wide range of sanitizing products</p>
  <div class="btn" style="left:150px;top:243px">Check price and availability</div>
  <div class="photo" style="left:790px;top:30px;width:325px;height:325px;background:linear-gradient(120deg,#6b4c38 0%,#9c7a60 40%,#cdb9a4 70%,#b49276 100%)" role="img" aria-label="Photo sanitizer tower in a rustic barn venue"></div>
</section>

<footer class="footer">
  <span style="left:150px">© 2021 Purvant, LLC</span>
  <span style="left:456px">Site Map</span>
  <span style="left:668px">Privacy Policy</span>
</footer>
<div class="social" aria-label="Social links">
  <i style="left:942px"></i>
  <i style="left:982px"></i>
  <i style="left:1021px"></i>
</div>

</body>
</html>
```